Environmental and Industrial Services Company Needs Brochure Design

We need a new brochure design for an established company that services the Southeastern United States. It is a highly diversified company that centers around Environmental and Industrial Services. The Environmental side revolved around emergency chemical and spill response, HAZMAT, hazardous/ non hazardous waste management, wastewater treatment, and remediation services (cleaning up contaminated sites). And the Industrial side utilizes heavy equipment like vacuum trucks and hydroblasters to clean process equipment inside of factories and manufacturing facilities. Predominantly our clients are large industrial clients, commercial clients, and the government. The people who would see the brochure are decision makers; engineers, project managers, procurement heads for large companies. These are serious and educated people who are looking for the best.

The designs should incorporate our colors and I welcome you to use any of the pictures from our website www.kvlterra.com EXCLUSIVELY FOR THIS PROJECT, of course. This brochure should communicate professionalism, confidence, stability, and portray the kind of company who efficiently manages complicated issues. Our site gives a better kind of idea of the branding we want to extend into the brochure and I caution any designer to NOT allow the environmental aspect of our company to lead them to design brochures more fitting for Green Tech companies or Alternative Energy.

Target Market(s)

Engineers, Factory Managers, Project Managers, Consultants, Heads of Large Companies, Service Managers

Industry/Entity Type

Industrial

Requirements
Must have
• The brochure must
-Be divided like the services section of our website w/ categories in this order:
-Industrial Services, Waste Management, Remediation Services, Emergency Response, Marine Services, Stormwater Services
-Owing to the large info in these sections, I'd recommend separate pages or tabs
-Incorporate our colors
-Use photos from the site

```html
<!DOCTYPE html>
<html lang="en">
<head>
<meta charset="utf-8">
<title>Company Profile Brochure</title>
<link href="https://fonts.googleapis.com/css2?family=Michroma&family=Tenor+Sans&family=Crimson+Text&display=swap" rel="stylesheet">
<style>
:root{
  --bg-light:#f6f6f6;
  --bg-dark:#dcdcdc;
  --blue-deep:#2463a6;
  --blue-bright:#0fd0ff;
  --blue-text:#2d62a8;
  --ink:#222;
  --body-text:#555;
  --charcoal:#2e2e2e;
  --slate:#5f5f5f;
  --paper:#f1f1f1;
}
*{margin:0;padding:0;box-sizing:border-box}
html,body{width:1200px;height:879px;overflow:hidden}
body{background:radial-gradient(ellipse at 40% 45%,var(--bg-light) 0%,#ececec 60%,var(--bg-dark) 100%);position:relative;font-family:"Crimson Text",serif}
.spread-title{position:absolute;font-family:"Michroma",sans-serif;font-size:19px;line-height:1;font-weight:400;color:var(--ink);letter-spacing:.5px;white-space:nowrap}
.spread-title.inside{left:775px;top:14px}
.spread-title.outside{left:765px;top:855px}
.panel{position:absolute;overflow:hidden;box-shadow:0 4px 14px rgba(0,0,0,.28)}
.panel svg.art{position:absolute;left:0;top:0;width:100%;height:100%}
.cover{left:110px;top:110px;width:330px;height:660px}
.cover-small{left:1001px;top:478px;width:192px;height:372px}
.cover-text{position:absolute;font-family:"Tenor Sans",sans-serif;line-height:1;white-space:nowrap}
.cover-title{color:var(--blue-text)}
.cover-logo{color:var(--slate)}
.cover .cover-title{left:140px;top:156px;font-size:21px}
.cover .cover-logo{left:150px;top:332px;font-size:20px}
.cover .logo-icon{position:absolute;left:20px;top:18px;font-family:"Tenor Sans",sans-serif;font-size:12px;line-height:1;color:#fff}
.cover-small .cover-title{left:76px;top:72px;font-size:12.5px}
.cover-small .cover-logo{left:85px;top:178px;font-size:11.5px;color:#333}
.inside-panel{top:55px;width:188px;height:373px}
.about{left:593px}
.services{left:799px}
.contact{left:1000px;width:186px}
.panel-heading{position:absolute;font-family:"Michroma",sans-serif;font-size:12.5px;line-height:1;font-weight:400;color:var(--ink);white-space:nowrap}
.about .panel-heading{left:34px;top:30px}
.services .panel-heading{left:36px;top:28px}
.section-label{position:absolute;left:13px;font-family:"Michroma",sans-serif;font-size:7.2px;line-height:1;font-weight:400;color:var(--blue-text);white-space:nowrap}
.lorem{position:absolute;left:13px;width:168px;font-size:5.4px;line-height:6.8px;color:var(--body-text)}
.photo{position:absolute}
.logo-slot{position:absolute;right:8px;bottom:4px;font-family:"Crimson Text",serif;font-size:11px;line-height:1.2;color:#fff;white-space:nowrap}
.contact .contact-heading{position:absolute;left:17px;top:34px;font-family:"Michroma",sans-serif;font-size:10px;line-height:1;font-weight:400;color:var(--blue-text);white-space:nowrap}
.contact address{position:absolute;left:11px;top:72px;font-style:normal;font-size:9px;line-height:10.6px;color:#555;white-space:nowrap}
.contact address p+p{margin-top:6px}
.outside-panel{top:481px;width:187px;height:369px}
.fold-left{left:582px}
.fold-center{left:788px}
</style>
</head>
<body>

<h1 class="spread-title inside">Brochure inside</h1>

<section class="panel cover" aria-label="Front cover">
  <svg class="art" viewBox="0 0 190 380" preserveAspectRatio="none">
    <defs>
      <radialGradient id="cover-blue" cx="0.25" cy="0.55" r="0.6">
        <stop offset="0" stop-color="var(--blue-bright)"/>
        <stop offset="1" stop-color="var(--blue-deep)"/>
      </radialGradient>
    </defs>
    <rect width="190" height="380" fill="var(--paper)"/>
    <path d="M60 240 Q135 222 190 228 L190 380 L70 380 Z" fill="var(--slate)"/>
    <path d="M0 0 L98 0 C60 60 52 150 56 230 C58 300 70 345 74 380 L0 380 Z" fill="url(#cover-blue)"/>
    <path d="M98 0 C60 60 52 150 56 230 C58 300 70 345 74 380" fill="none" stroke="var(--charcoal)" stroke-width="4"/>
  </svg>
  <span class="logo-icon">Logo Icon Only here</span>
  <span class="cover-text cover-title">Company Profile</span>
  <span class="cover-text cover-logo">Your Logo here</span>
</section>

<section class="panel inside-panel about" aria-label="About Us panel">
  <svg class="art" viewBox="0 0 188 373" preserveAspectRatio="none">
    <defs>
      <linearGradient id="about-paper" x1="0" y1="0" x2="0" y2="1">
        <stop offset="0" stop-color="#f5f5f5"/><stop offset="1" stop-color="#dadada"/>
      </linearGradient>
      <linearGradient id="about-blue" x1="0" y1="0" x2="1" y2="0">
        <stop offset="0" stop-color="var(--blue-deep)"/><stop offset="0.6" stop-color="#1aa6e8"/><stop offset="1" stop-color="var(--blue-deep)"/>
      </linearGradient>
    </defs>
    <rect width="188" height="373" fill="url(#about-paper)"/>
    <path d="M0 332 Q100 318 188 300 L188 373 L0 373 Z" fill="url(#about-blue)"/>
    <path d="M0 331 Q100 317 188 299" fill="none" stroke="#fff" stroke-width="1.5"/>
  </svg>
  <h2 class="panel-heading">About Us</h2>
  <p class="lorem" style="top:59px">Lorem ipsum dolor sit amet, consectetur adipisicing elit, sed do eiusmod tempor incididunt ut labore et dolore magna Lorem ipsum dolor sit amet, consectetur adipisicing elit, sed do eiusmod tempor incididunt ut labore et dolore magna</p>
  <h3 class="section-label" style="top:105px">Mission</h3>
  <p class="lorem" style="top:119px">Lorem ipsum dolor sit amet, consectetur adipisicing elit, sed do eiusmod tempor incididunt ut labore et dolore magna</p>
  <h3 class="section-label" style="top:144px">Vision</h3>
  <p class="lorem" style="top:157px">Lorem ipsum dolor sit amet, consectetur adipisicing elit, sed do eiusmod tempor incididunt ut labore et dolore magna</p>
  <h3 class="section-label" style="top:186px">Objectives</h3>
  <p class="lorem" style="top:201px">Lorem ipsum dolor sit amet, consectetur adipisicing elit, sed do eiusmod tempor incididunt ut labore et dolore magna</p>
  <h3 class="section-label" style="top:227px">Expertise</h3>
  <p class="lorem" style="top:241px">Lorem ipsum dolor sit amet, consectetur adipisicing elit, sed do eiusmod tempor incididunt ut labore et dolore magna</p>
  <div class="photo" role="img" aria-label="Photo of a service truck at a work site" style="left:0;top:256px;width:101px;height:76px;background:linear-gradient(180deg,#9fb4c2,#8a8a80);opacity:.75"></div>
  <div class="photo" role="img" aria-label="Photo of a crew member in protective gear" style="left:101px;top:256px;width:87px;height:62px;background:linear-gradient(180deg,#c9a08a,#b0623e);opacity:.7"></div>
  <span class="logo-slot">Your Logo here</span>
</section>

<section class="panel inside-panel services" aria-label="Our Services panel">
  <svg class="art" viewBox="0 0 188 373" preserveAspectRatio="none">
    <defs>
      <linearGradient id="services-paper" x1="0" y1="0" x2="0" y2="1">
        <stop offset="0" stop-color="#f5f5f5"/><stop offset="1" stop-color="#dadada"/>
      </linearGradient>
      <linearGradient id="services-blue" x1="0" y1="0" x2="1" y2="0">
        <stop offset="0" stop-color="var(--blue-deep)"/><stop offset="0.6" stop-color="#1aa6e8"/><stop offset="1" stop-color="var(--blue-deep)"/>
      </linearGradient>
    </defs>
    <rect width="188" height="373" fill="url(#services-paper)"/>
    <path d="M0 332 Q100 318 188 300 L188 373 L0 373 Z" fill="url(#services-blue)"/>
    <path d="M0 331 Q100 317 188 299" fill="none" stroke="#fff" stroke-width="1.5"/>
  </svg>
  <h2 class="panel-heading">Our Services</h2>
  <div class="photo" role="img" aria-label="Photo of a service truck at a work site" style="left:0;top:270px;width:101px;height:62px;background:linear-gradient(180deg,#9fb4c2,#8a8a80);opacity:.75"></div>
  <div class="photo" role="img" aria-label="Photo of a crew member in protective gear" style="left:101px;top:270px;width:87px;height:48px;background:linear-gradient(180deg,#c9a08a,#b0623e);opacity:.7"></div>
  <h3 class="section-label" style="top:62px">Industrial Services</h3>
  <p class="lorem" style="top:76px">Lorem ipsum dolor sit amet, consectetur adipisicing elit, sed do eiusmod tempor incididunt ut labore et dolore magna</p>
  <h3 class="section-label" style="top:102px">Waste Management</h3>
  <p class="lorem" style="top:116px">Lorem ipsum dolor sit amet, consectetur adipisicing elit, sed do eiusmod tempor incididunt ut labore et dolore magna</p>
  <h3 class="section-label" style="top:142px">Remediation</h3>
  <p class="lorem" style="top:156px">Lorem ipsum dolor sit amet, consectetur adipisicing elit, sed do eiusmod tempor incididunt ut labore et dolore magna</p>
  <h3 class="section-label" style="top:184px">Emergency Response</h3>
  <p class="lorem" style="top:199px">Lorem ipsum dolor sit amet, consectetur adipisicing elit, sed do eiusmod tempor incididunt ut labore et dolore magna</p>
  <h3 class="section-label" style="top:225px">Marine Services</h3>
  <p class="lorem" style="top:239px">Lorem ipsum dolor sit amet, consectetur adipisicing elit, sed do eiusmod tempor incididunt ut labore et dolore magna</p>
  <h3 class="section-label" style="top:267px">StormWater Services</h3>
  <p class="lorem" style="top:281px">Lorem ipsum dolor sit amet, consectetur adipisicing elit, sed do eiusmod tempor incididunt ut labore et dolore magna</p>
  <span class="logo-slot">Your Logo here</span>
</section>

<section class="panel inside-panel contact" aria-label="Contact panel">
  <svg class="art" viewBox="0 0 186 373" preserveAspectRatio="none">
    <defs>
      <linearGradient id="contact-paper" x1="0" y1="0" x2="0" y2="1">
        <stop offset="0" stop-color="#f5f5f5"/><stop offset="1" stop-color="#dadada"/>
      </linearGradient>
      <radialGradient id="contact-blue" cx="0.85" cy="0.5" r="0.7">
        <stop offset="0" stop-color="var(--blue-bright)"/><stop offset="1" stop-color="var(--blue-deep)"/>
      </radialGradient>
    </defs>
    <rect width="186" height="373" fill="url(#contact-paper)"/>
    <path d="M112 0 C140 40 142 120 140 200 C138 280 132 330 128 373 L186 373 L186 0 Z" fill="url(#contact-blue)"/>
    <path d="M112 0 C140 40 142 120 140 200 C138 280 132 330 128 373" fill="none" stroke="var(--charcoal)" stroke-width="3"/>
  </svg>
  <h2 class="contact-heading">Contact info</h2>
  <address>
    <p>Harbor Lane, Kelvin Park<br>New York, USA</p>
    <p>Tel # 0000000000<br>Fax # 0000000000<br>Email Id: info@kvlterra.com<br>Website: www.kvlterra.com</p>
  </address>
  <div class="photo" role="img" aria-label="Photo of an industrial services plant" style="left:0;top:210px;width:128px;height:42px;background:linear-gradient(180deg,#6f8fae,#3a4a5a)"></div>
  <div class="photo" role="img" aria-label="Photo of an emergency spill response on land and water" style="left:0;top:254px;width:128px;height:40px;background:linear-gradient(180deg,#9cc6e6,#c08a3a)"></div>
  <div class="photo" role="img" aria-label="Photo of remediation services with heavy equipment" style="left:0;top:296px;width:128px;height:38px;background:linear-gradient(180deg,#7aa0c0,#c8a040)"></div>
  <div class="photo" role="img" aria-label="Photo of waste management drums" style="left:0;top:336px;width:128px;height:37px;background:linear-gradient(180deg,#b0704a,#7a4a30)"></div>
</section>

<section class="panel outside-panel fold-left" aria-label="Outside left fold">
  <svg class="art" viewBox="0 0 187 376" preserveAspectRatio="none">
    <defs>
      <linearGradient id="fold-left-blue" x1="0" y1="0" x2="1" y2="1">
        <stop offset="0" stop-color="var(--blue-deep)"/><stop offset="0.5" stop-color="#2a8ad0"/><stop offset="1" stop-color="var(--blue-deep)"/>
      </linearGradient>
    </defs>
    <rect width="187" height="376" fill="url(#fold-left-blue)"/>
    <path d="M0 145 Q60 150 187 112 L187 238 Q80 212 0 232 Z" fill="var(--paper)"/>
    <path d="M0 146 Q60 151 187 113 L187 122 Q70 158 0 158 Z" fill="var(--charcoal)"/>
    <path d="M0 222 Q80 205 187 232 L187 242 Q80 218 0 234 Z" fill="var(--charcoal)"/>
  </svg>
</section>

<section class="panel outside-panel fold-center" aria-label="Outside center fold">
  <svg class="art" viewBox="0 0 187 376" preserveAspectRatio="none">
    <defs>
      <radialGradient id="fold-center-blue" cx="0.5" cy="0.55" r="0.7">
        <stop offset="0" stop-color="var(--blue-bright)"/><stop offset="1" stop-color="var(--blue-deep)"/>
      </radialGradient>
    </defs>
    <rect width="187" height="376" fill="url(#fold-center-blue)"/>
    <path d="M0 112 Q120 70 187 130 L187 232 Q120 280 0 262 Z" fill="var(--paper)"/>
    <path d="M0 104 Q110 82 165 100 Q90 90 0 116 Z" fill="var(--charcoal)"/>
    <path d="M0 258 Q80 272 187 232 Q100 270 0 274 Z" fill="var(--charcoal)"/>
  </svg>
</section>

<section class="panel cover-small" aria-label="Front cover panel">
  <svg class="art" viewBox="0 0 190 380" preserveAspectRatio="none">
    <defs>
      <radialGradient id="cover-small-blue" cx="0.25" cy="0.55" r="0.6">
        <stop offset="0" stop-color="var(--blue-bright)"/>
        <stop offset="1" stop-color="var(--blue-deep)"/>
      </radialGradient>
    </defs>
    <rect width="190" height="380" fill="var(--paper)"/>
    <path d="M70 240 Q135 215 190 220 L190 380 L75 380 Z" fill="var(--slate)"/>
    <path d="M0 0 L98 0 C60 60 52 150 56 230 C58 300 84 345 88 380 L0 380 Z" fill="url(#cover-small-blue)"/>
    <path d="M98 0 C60 60 52 150 56 230 C58 300 84 345 88 380" fill="none" stroke="var(--charcoal)" stroke-width="3"/>
  </svg>
  <span class="cover-text cover-title">Company Profile</span>
  <span class="cover-text cover-logo">Your Logo here</span>
</section>

<h1 class="spread-title outside">Brochure Outside</h1>

</body>
</html>
```